Real Estate Listing Signs for standard Yard arms

I need real estate listing signs done, for the standard sized sign to be hung beneath a white yard arm. To match existing logo. Information to be included:
-Logo
-Business name
-Phone number
-Marden Fosk Tundra Circle & Marden Fosk Realty logos (smaller print)

Colors to be Red and anywhere in the gray scale between black and white, or a combination of those.

Target Market(s)

Drive by visuals

Industry/Entity Type

Real Estate Agent

Colors

Designer to choose only greyscale colors for use in the design.

Requirements
Must have
• My Logo and business name in same/similar font to whats provided, the MF tundra circle logo (small on bottom or corner somewhere), My phone number, and a decent amount of red coloration on the sign.

```html
<!DOCTYPE html>
<html lang="en">
<head>
<meta charset="utf-8">
<title>Vessler Realty – Yard Arm Listing Sign</title>
<link rel="stylesheet" href="https://fonts.googleapis.com/css2?family=Bebas+Neue&family=Barlow+Semi+Condensed:wght@600&family=Poppins:wght@400;500;600&display=swap">
<style>
  :root {
    --red: #e32b24;
    --black: #111111;
    --charcoal: #1b1b1b;
    --white: #ffffff;
    --paper: #efefef;
    --paper-light: #fafafa;
    --grey-text: #6e6e6e;
    --page: #d9d9d9;
  }
  * { margin: 0; padding: 0; box-sizing: border-box; }
  html, body { width: 960px; height: 1200px; overflow: hidden; background: var(--page); }
  .canvas { position: relative; width: 960px; height: 1200px; }
  .sign {
    position: absolute; left: 0; top: 256px;
    width: 1200px; height: 858px;
    transform: scale(0.8); transform-origin: 0 0;
    overflow: hidden;
    background: linear-gradient(180deg, var(--paper-light) 0%, var(--paper) 100%);
  }
  .sign-shapes { position: absolute; inset: 0; }
  .skyline-photo {
    position: absolute; left: 0; top: 140px; width: 770px; height: 300px;
    background: linear-gradient(180deg, rgba(255,255,255,0) 0%, rgba(170,170,170,0.45) 55%, rgba(255,255,255,0) 100%);
  }
  .agent-photo {
    position: absolute; left: 660px; top: 268px; width: 460px; height: 590px;
    border-radius: 200px 200px 0 0;
    background: radial-gradient(ellipse at 60% 28%, #4a3a30 0%, #2a2725 38%, #141414 78%);
  }
  .brand-title {
    position: absolute; left: 36px; top: 44px;
    font-family: "Bebas Neue", sans-serif; font-size: 140px; line-height: 122px;
  }
  .brand-title .line-red { color: var(--red); display: block; }
  .brand-title .line-black { color: var(--black); display: block; }
  .agent-bar {
    position: absolute; left: 0; top: 315px; width: 512px; height: 95px;
    background: var(--black);
    clip-path: polygon(0 0, 84% 0, 100% 100%, 0 100%);
  }
  .agent-name {
    position: absolute; left: 36px; top: 333px;
    font-family: "Barlow Semi Condensed", sans-serif; font-weight: 600;
    font-size: 54px; line-height: 60px; color: var(--white);
  }
  .contact {
    position: absolute; left: 36px; top: 457px;
    font-family: "Poppins", sans-serif; font-weight: 500;
    font-size: 42px; line-height: 68px; color: var(--black);
  }
  .contact-rule {
    position: absolute; left: 36px; top: 602px; width: 447px; height: 7px;
    background: var(--red);
  }
  .disclaimer {
    position: absolute; left: 36px; top: 632px;
    font-family: "Poppins", sans-serif; font-weight: 400;
    font-size: 30px; line-height: 50px; color: var(--black);
  }
  .brokerage {
    position: absolute; left: 38px; top: 748px;
    font-family: "Poppins", sans-serif; font-weight: 600; color: var(--grey-text);
  }
  .brokerage-name { font-size: 34px; line-height: 40px; letter-spacing: -0.5px; text-transform: uppercase; }
  .brokerage-sub { font-size: 18px; line-height: 22px; font-weight: 400; text-transform: uppercase; }
  .client-mark {
    position: absolute; left: 800px; top: 98px;
    display: flex; align-items: center; gap: 22px;
  }
  .client-mark-square { width: 64px; height: 64px; background: var(--red); }
  .client-mark-name {
    font-family: "Poppins", sans-serif; font-weight: 600;
    font-size: 40px; line-height: 54px; color: var(--white); text-transform: uppercase;
  }
</style>
</head>
<body>
<main class="canvas">
  <section class="sign" aria-label="Vessler Realty yard arm listing sign">
    <div class="skyline-photo" role="img" aria-label="Faded grey photograph of a city skyline"></div>

    <svg class="sign-shapes" viewBox="0 0 1200 858" width="1200" height="858" aria-hidden="true">
      <polygon class="panel-dark" points="530,0 1200,0 1200,858 1070,858 760,520 770,460" fill="var(--charcoal)"/>
      <polygon class="panel-red-band" points="410,0 530,0 770,460 770,585" fill="var(--red)"/>
      <polygon class="panel-light-strip" points="700,540 760,520 1070,858 1010,858" fill="var(--paper)"/>
    </svg>

    <div class="agent-photo" role="img" aria-label="Photograph of the agent in a black shirt pointing toward the contact details"></div>

    <h1 class="brand-title">
      <span class="line-red">Vessler</span>
      <span class="line-black">Realty</span>
    </h1>

    <div class="agent-bar"></div>
    <p class="agent-name">JORDAN VESSLER</p>

    <p class="contact">
      <span class="contact-phone">907-555-0148</span><br>
      <span class="contact-email">jvessler@mailbox.com</span>
    </p>
    <div class="contact-rule"></div>

    <p class="disclaimer">Each Office Independently Owned<br>and Operated</p>

    <div class="brokerage">
      <p class="brokerage-name">MF Tundra Circle</p>
      <p class="brokerage-sub">Marden Fosk Realty</p>
    </div>

    <div class="client-mark">
      <span class="client-mark-square"></span>
      <span class="client-mark-name">Vessler<br>Realty</span>
    </div>
  </section>
</main>
</body>
</html>
```